Studying Effectively To Do List

I am looking to design a new "Study To Do List" for High School students (Ages 15 - 18) . This will be printed as an A4 notepad and so should only be a single A4 page.

The Design will need to be professional and look semi-serious but also be appealing to High school students (Ages 15 - 18) and should NOT be gender specific.

I have attached a word document outlining the structure of the page. The space provided should be large enough that people can write in it comfortably.

The notepad will most likely be printed in black and white but I'm also looking at coloured options - colours should be kept to a minimum.

This will be printed professionally and should also include a 3mm bleed.

The design should also include the business logo (included in the word document)

Target Market(s)

High School students (Ages 15 - 18). Both genders

Industry/Entity Type

Education

Font styles to use
Serif
Sans Serif

Requirements
Must have
• Please see the word document attached.
Should not have
• Too much colour

```html
<!DOCTYPE html>
<html lang="en">
<head>
<meta charset="utf-8">
<title>Study To Do List</title>
<link href="https://fonts.googleapis.com/css2?family=Exo+2:ital,wght@1,600;1,700&display=swap" rel="stylesheet">
<style>
:root{
  --paper:#ffffff;
  --panel:#959aa1;
  --tab:#5b6670;
  --ink:#ffffff;
  --muted:#4a525a;
  --rule:#8e939a;
  --accent:#e8772e;
  --navy:#243649;
}
*{box-sizing:border-box;margin:0;padding:0}
html,body{width:849px;height:1200px;overflow:hidden;background:var(--paper)}
body{position:relative;font-family:"Exo 2",sans-serif;font-style:italic;font-weight:700;color:var(--ink)}
.brand{position:absolute;right:40px;top:44px;display:flex;align-items:center;gap:8px;font-size:19px;color:var(--navy);letter-spacing:0.5px}
.brand-dot{width:14px;height:14px;border-radius:50%;background:var(--accent)}
.date{position:absolute;left:28px;top:99px;display:flex;gap:4px}
.date-label{width:64px;height:24px;background:var(--tab);font-size:13px;letter-spacing:2px;line-height:24px;padding-left:9px}
.date-box{width:25px;height:24px;border:1px solid #b8bcc1;background:var(--paper)}
.sheet{position:absolute;left:28px;top:134px;width:794px;height:906px;background:var(--panel)}
.field{background:var(--paper);height:24px;flex:1}
.tab{background:var(--tab);height:24px;font-size:12px;letter-spacing:2.4px;line-height:24px}
.revision{position:absolute;left:12px;top:12px;display:grid;grid-template-columns:383px 371px;column-gap:16px;row-gap:4.3px}
.rev-row{display:flex;align-items:center;height:24px}
.rev-row .num{font-size:12px;width:29px;padding-left:3px}
.rev-row.right .num{width:16px;padding-left:0}
.rev-row .tab{width:95px;padding-left:7px}
.rev-row .first{width:33px;text-align:center;padding:0}
.heading{position:absolute;left:141px;font-size:17px;letter-spacing:5px}
.homework-head{top:147px}
.assess-head{top:531px}
.list{position:absolute;left:12px;width:770px;display:flex;flex-direction:column;gap:4.3px}
.homework{top:171px}
.assessments{top:558px}
.row{display:flex;gap:4px;height:24px}
.row .tab,.row .sub{width:124px;flex:none;text-align:right;padding-right:16px}
.row .sub{font-size:12px;letter-spacing:2.4px;line-height:24px}
.assessments .tab,.assessments .sub{text-align:center;padding-right:0;letter-spacing:2px}
.row .main{flex:none;width:386px}
.row .due{width:42px;flex:none;text-align:center;letter-spacing:1.5px;padding:0}
.vlabel{position:absolute;font-size:11px;letter-spacing:3px;color:var(--muted);transform:rotate(-90deg);transform-origin:left top;white-space:nowrap}
.notes-label{left:29px;top:1162px}
.practice-label{left:444px;top:1164px}
.line{position:absolute;height:18px;border-bottom:1px solid var(--rule);font-size:11px;line-height:16px;color:var(--muted)}
</style>
</head>
<body>
<div class="brand"><span class="brand-dot"></span>Velmora Learning</div>

<div class="date">
  <div class="date-label">DATE</div>
  <div class="date-box"></div><div class="date-box"></div><div class="date-box"></div><div class="date-box"></div>
  <div class="date-box"></div><div class="date-box"></div><div class="date-box"></div><div class="date-box"></div>
</div>

<main class="sheet">
  <section class="revision">
    <div class="rev-row"><div class="tab">REVISION</div><div class="num first">1</div><div class="field"></div></div>
    <div class="rev-row right"><div class="num">5</div><div class="field"></div></div>
    <div class="rev-row"><div class="num">2</div><div class="field"></div></div>
    <div class="rev-row right"><div class="num">6</div><div class="field"></div></div>
    <div class="rev-row"><div class="num">3</div><div class="field"></div></div>
    <div class="rev-row right"><div class="num">7</div><div class="field"></div></div>
    <div class="rev-row"><div class="num">4</div><div class="field"></div></div>
    <div class="rev-row right"><div class="num">8</div><div class="field"></div></div>
  </section>

  <h2 class="heading homework-head">HOMEWORK</h2>
  <section class="list homework">
    <div class="row"><div class="tab">SUBJECT</div><div class="field"></div></div>
    <div class="row"><div class="sub">TASK</div><div class="field"></div></div>
    <div class="row"><div class="tab">SUBJECT</div><div class="field"></div></div>
    <div class="row"><div class="sub">TASK</div><div class="field"></div></div>
    <div class="row"><div class="tab">SUBJECT</div><div class="field"></div></div>
    <div class="row"><div class="sub">TASK</div><div class="field"></div></div>
    <div class="row"><div class="tab">SUBJECT</div><div class="field"></div></div>
    <div class="row"><div class="sub">TASK</div><div class="field"></div></div>
    <div class="row"><div class="tab">SUBJECT</div><div class="field"></div></div>
    <div class="row"><div class="sub">TASK</div><div class="field"></div></div>
    <div class="row"><div class="tab">SUBJECT</div><div class="field"></div></div>
    <div class="row"><div class="sub">TASK</div><div class="field"></div></div>
  </section>

  <h2 class="heading assess-head">ASSESSMENTS</h2>
  <section class="list assessments">
    <div class="row"><div class="tab">ASSESSMENTS</div><div class="field main"></div><div class="tab due">DUE</div><div class="field"></div></div>
    <div class="row"><div class="sub">ELEMENT</div><div class="field"></div></div>
    <div class="row"><div class="tab">ASSESSMENTS</div><div class="field main"></div><div class="tab due">DUE</div><div class="field"></div></div>
    <div class="row"><div class="sub">ELEMENT</div><div class="field"></div></div>
    <div class="row"><div class="tab">ASSESSMENTS</div><div class="field main"></div><div class="tab due">DUE</div><div class="field"></div></div>
    <div class="row"><div class="sub">ELEMENT</div><div class="field"></div></div>
    <div class="row"><div class="tab">ASSESSMENTS</div><div class="field main"></div><div class="tab due">DUE</div><div class="field"></div></div>
    <div class="row"><div class="sub">ELEMENT</div><div class="field"></div></div>
    <div class="row"><div class="tab">ASSESSMENTS</div><div class="field main"></div><div class="tab due">DUE</div><div class="field"></div></div>
    <div class="row"><div class="sub">ELEMENT</div><div class="field"></div></div>
    <div class="row"><div class="tab">ASSESSMENTS</div><div class="field main"></div><div class="tab due">DUE</div><div class="field"></div></div>
    <div class="row"><div class="sub">ELEMENT</div><div class="field"></div></div>
  </section>
</main>

<div class="vlabel notes-label">NOTES</div>
<div class="line" style="left:58px;top:1067px;width:184px">1</div>
<div class="line" style="left:58px;top:1094px;width:184px">2</div>
<div class="line" style="left:58px;top:1120px;width:184px">3</div>
<div class="line" style="left:58px;top:1148px;width:184px">4</div>
<div class="line" style="left:249px;top:1067px;width:184px">5</div>
<div class="line" style="left:249px;top:1094px;width:184px">6</div>
<div class="line" style="left:249px;top:1120px;width:184px">7</div>
<div class="line" style="left:249px;top:1148px;width:184px">8</div>
<div class="vlabel practice-label">PRACTICE</div>
<div class="line" style="left:470px;top:1067px;width:340px"></div>
<div class="line" style="left:470px;top:1094px;width:340px"></div>
<div class="line" style="left:470px;top:1120px;width:340px"></div>
<div class="line" style="left:470px;top:1148px;width:340px"></div>
</body>
</html>
```